Letterhead Design Needed for Real Estate Office

We are a boutique real estate agency focused on property management. We need a letter head which is professional looking and include the following information:

Logo
ABN Number
Address
Postal Address
Phone
Fax
Mobile
Email
Website

Please note that the PLVAQT logo can not be changed and must be positioned at the bottom right corner.

Please find attached the existing letterhead design for all the required elements.

Target Market(s)

Letterhead mostly used for service of notices, business letters, clients communication

Industry/Entity Type

Boutique

Colors

Designer to choose colors to be used in the design.

Requirements
Must have
• Logo

```html
<!DOCTYPE html>
<html lang="en">
<head>
<meta charset="utf-8">
<title>Kestrel Realty Letterhead</title>
<link href="https://fonts.googleapis.com/css2?family=Lato:wght@400;700&display=swap" rel="stylesheet">
<style>
  :root {
    --sheet: #ffffff;
    --grey-deep: #d3d4d6;
    --grey-soft: #e6e7e9;
    --ink: #1d1d1f;
    --brand-ink: #2b2b2d;
    --brand-dot: #8a8c8f;
    --badge-blue: #1f5fa8;
    --badge-navy: #1b2a4a;
  }
  * { margin: 0; padding: 0; box-sizing: border-box; }
  html, body {
    width: 848px; height: 1200px; overflow: hidden;
    background: var(--sheet);
  }
  .letterhead {
    position: relative; width: 848px; height: 1200px;
    overflow: hidden; background: var(--sheet);
    font-family: "Lato", sans-serif; color: var(--ink);
  }
  .backdrop { position: absolute; inset: 0; }
  .brand {
    position: absolute; left: 522px; top: 86px;
    display: flex; align-items: center; gap: 12px;
  }
  .brand-dot {
    width: 30px; height: 30px; border-radius: 50%;
    background: var(--brand-dot);
  }
  .brand-name {
    font-weight: 700; font-size: 26px; line-height: 1;
    letter-spacing: 1px; color: var(--brand-ink);
    text-transform: uppercase; white-space: nowrap;
  }
  .contact {
    position: absolute; left: 54px; top: 1068px;
    font-size: 13.5px; line-height: 24px; color: var(--ink);
  }
  .contact-row { display: flex; align-items: center; gap: 22px; white-space: nowrap; }
  .contact-item { display: inline-flex; align-items: center; gap: 9px; }
  .icon { width: 12px; height: 12px; fill: var(--ink); flex: none; }
  .member-badge {
    position: absolute; left: 618px; top: 1066px;
    display: flex; align-items: center; gap: 10px;
  }
  .member-square {
    width: 34px; height: 34px; background: var(--badge-blue);
  }
  .member-name {
    font-weight: 700; font-size: 34px; letter-spacing: -0.5px;
    color: var(--badge-navy);
  }
</style>
</head>
<body>
<div class="letterhead">
  <svg class="backdrop" width="848" height="1200" viewBox="0 0 848 1200" aria-hidden="true">
    <defs>
      <linearGradient id="footFade" x1="0" y1="0" x2="0" y2="1">
        <stop offset="0" stop-color="#ffffff"/>
        <stop offset="1" stop-color="#d9dadc"/>
      </linearGradient>
    </defs>
    <rect class="header-band" x="0" y="0" width="848" height="560" fill="var(--grey-deep)"/>
    <path class="header-sweep" d="M0 0 L40 0 Q260 70 520 150 Q240 190 120 300 L88 405 L0 60 Z" fill="var(--grey-soft)"/>
    <ellipse class="header-curve" cx="440" cy="727" rx="560" ry="577" fill="var(--sheet)"/>
    <rect class="footer-band" x="0" y="940" width="848" height="260" fill="url(#footFade)"/>
    <ellipse class="footer-curve" cx="424" cy="560" rx="980" ry="475" fill="var(--sheet)"/>
  </svg>

  <header class="brand">
    <span class="brand-dot"></span>
    <span class="brand-name">Kestrel Realty</span>
  </header>

  <footer class="contact">
    <div class="contact-row">ABN 42 508 316 774</div>
    <div class="contact-row">
      <span class="contact-item">
        <svg class="icon" viewBox="0 0 12 12"><path d="M6 1 L11.5 6 H10 V11 H7.3 V8 H4.7 V11 H2 V6 H0.5 Z"/></svg>
        18B 210-232 Harbour Street Lindfield NSW 2070 AUSTRALIA
      </span>
    </div>
    <div class="contact-row">
      <span class="contact-item">
        <svg class="icon" viewBox="0 0 12 12"><path d="M6 1 L11.5 6 H10 V11 H7.3 V8 H4.7 V11 H2 V6 H0.5 Z"/></svg>
        PO Box 412 Lindfield NSW 2070
      </span>
      <span class="contact-item">
        <svg class="icon" viewBox="0 0 12 12"><path d="M3.5 0.5 H8.5 V11.5 H3.5 Z M4.5 2 V8.5 H7.5 V2 Z M5.5 9.5 H6.5 V10.5 H5.5 Z" fill-rule="evenodd"/></svg>
        0400 512 736
      </span>
      <span class="contact-item">
        <svg class="icon" viewBox="0 0 12 12"><path d="M1 4 Q6 0.5 11 4 L9.5 5.5 L8 4.5 H4 L2.5 5.5 Z M3 7 H9 L10 10.5 H2 Z"/></svg>
        9000 3158
      </span>
    </div>
    <div class="contact-row">
      <span class="contact-item">
        <svg class="icon" viewBox="0 0 12 12"><path d="M3 0.5 H9 V4 H3 Z M1 4.5 H11 V9 H9 V11.5 H3 V9 H1 Z M4 8 V10.5 H8 V8 Z" fill-rule="evenodd"/></svg>
        9000 3159
      </span>
      <span class="contact-item">
        <svg class="icon" viewBox="0 0 12 12"><path d="M6 0.8 A5.2 5.2 0 1 0 10 9.3 L9.2 8.6 A4.1 4.1 0 1 1 10.1 6 V6.9 Q10.1 8 9.1 8 Q8.2 8 8.2 6.9 V3.3 H7.2 V3.8 A2.6 2.6 0 1 0 7.5 8.1 Q8 9.1 9.1 9.1 Q11.2 9.1 11.2 6.9 V6 A5.2 5.2 0 0 0 6 0.8 Z M6 4.3 A1.7 1.7 0 1 1 6 7.7 A1.7 1.7 0 1 1 6 4.3 Z" fill-rule="evenodd"/></svg>
        hello@kestrelrealty.cc
      </span>
      <span class="contact-item">
        <svg class="icon" viewBox="0 0 12 12"><path d="M1.5 2 H10.5 V8 H1.5 Z M0 9 H12 V10.5 H0 Z"/></svg>
        www.kestrelrealty.cc
      </span>
    </div>
  </footer>

  <div class="member-badge">
    <span class="member-square"></span>
    <span class="member-name">PLVAQT</span>
  </div>
</div>
</body>
</html>
```